Online video and marketing company business cards

Need to get some new business cards designed to fit with our new logo. The cards should be professional, clean and simple.

Cards should have:

Name
Position
2 line address
telephone
mobile
email address
web address

We need to have our logo and if possible say what we do...
ONLINE FILM PRODUCTION & STRATEGY

Marketing

```html
<!DOCTYPE html>
<html lang="en">
<head>
<meta charset="utf-8">
<title>lumenframe business cards</title>
<link rel="stylesheet" href="https://fonts.googleapis.com/css2?family=Source+Sans+3:wght@400;600;700&display=swap">
<style>
  :root {
    --navy: #0b4770;
    --navy-deep: #083a5d;
    --sky: #74a9c9;
    --sky-soft: #5f94b6;
    --paper: #ffffff;
    --backdrop: #e9edf1;
  }
  * { box-sizing: border-box; margin: 0; padding: 0; }
  html, body {
    width: 1200px; height: 1024px; overflow: hidden;
    background: var(--backdrop);
    font-family: "Source Sans 3", "Myriad Pro", Arial, sans-serif;
  }
  .canvas { position: relative; width: 1200px; height: 1024px; }
  .card {
    position: absolute; width: 726px; height: 412px;
    border-radius: 30px; overflow: hidden;
    box-shadow: 0 6px 14px rgba(0,0,0,.28);
  }
  .card-front { left: 48px; top: 77px; background: var(--navy); }
  .card-back {
    left: 388px; top: 550px;
    background: linear-gradient(180deg, var(--navy) 0%, var(--navy-deep) 100%);
  }
  .front-shape { position: absolute; inset: 0; }
  .details { position: absolute; left: 50px; top: 66px; color: var(--paper); }
  .person-name { font-size: 25px; font-weight: 700; letter-spacing: .3px; line-height: 1; }
  .person-role { font-size: 17px; margin-top: 8px; }
  .address { font-size: 20px; line-height: 26px; margin-top: 26px; }
  .contacts { list-style: none; margin-top: 34px; font-size: 19px; line-height: 23px; }
  .contacts li { display: flex; align-items: center; gap: 6px; }
  .contacts svg { width: 12px; height: 12px; fill: #c9d8e4; flex: none; }
  .wordmark { position: absolute; display: flex; align-items: center; font-weight: 600; color: var(--sky); letter-spacing: -.5px; }
  .wordmark .dot { border-radius: 50%; background: var(--sky); }
  .wordmark-front { left: 404px; top: 178px; font-size: 46px; gap: 10px; }
  .wordmark-front .dot { width: 34px; height: 34px; }
  .wordmark-back { left: 170px; top: 168px; font-size: 64px; gap: 14px; }
  .wordmark-back .dot { width: 48px; height: 48px; }
  .back-url {
    position: absolute; left: 0; right: 0; top: 352px;
    text-align: center; color: var(--paper); font-size: 19px;
  }
</style>
</head>
<body>
<main class="canvas">
  <section class="card card-front">
    <svg class="front-shape" viewBox="0 0 726 412" aria-hidden="true">
      <path d="M452 0 C330 80 322 300 470 412 L500 412 C360 300 368 90 478 0 Z" fill="var(--sky-soft)"/>
      <path d="M478 0 C368 90 360 300 500 412 L520 412 C372 300 380 92 494 0 Z" fill="var(--navy)"/>
      <path d="M494 0 C380 92 372 300 520 412 L726 412 L726 0 Z" fill="var(--paper)"/>
    </svg>
    <div class="details">
      <h1 class="person-name">MARCUS ELLERY</h1>
      <p class="person-role">Job Title</p>
      <p class="address">Your Address Goes Here,<br>City, Zip Code, State</p>
      <ul class="contacts">
        <li><svg viewBox="0 0 12 12"><rect x="3" y="0" width="6" height="12" rx="1"/></svg>000 000 0000</li>
        <li><svg viewBox="0 0 12 12"><path d="M2 0h3l1 3-2 1.5c.8 1.8 2 3 3.5 3.5L9 6l3 1v3c0 1-1 2-2 2C5 12 0 7 0 2 0 1 1 0 2 0z"/></svg>+00 0 0000 0000</li>
        <li><svg viewBox="0 0 12 12"><rect x="3" y="0" width="6" height="4"/><rect x="0" y="4" width="12" height="5" rx="1"/><rect x="3" y="8" width="6" height="4"/></svg>+00 0 0000 0000</li>
        <li><svg viewBox="0 0 12 12"><circle cx="6" cy="6" r="6"/></svg>www.lumenframe.com</li>
        <li><svg viewBox="0 0 12 12"><path d="M0 2h12v8H0z"/></svg>name@lumenframe.com</li>
      </ul>
    </div>
    <div class="wordmark wordmark-front"><span class="dot"></span><span>lumenframe</span></div>
  </section>

  <section class="card card-back">
    <div class="wordmark wordmark-back"><span class="dot"></span><span>lumenframe</span></div>
    <p class="back-url">www.lumenframe.com</p>
  </section>
</main>
</body>
</html>
```